Bref créative
Summit Fairway Swing Institute
Elevating Every Swing
Professional
Brian Lockwell
Founder
(no physical address to be printed on business card or stationary)
brian@sfsinstitute.net
www.sfsinstitute.net
(Please include the RMX, DORAL and PLUF logos somewhere on the card)
* Full Round Review (FRR)
* On Course Coaching Sessions
* Junior Tournament Prep
* PLUF Beginner Classes
* Corporate Events
* Birthday Parties
Main company logo
Affiliation logo
Affiliation logo (on back of card)

```html
<!DOCTYPE html>
<html lang="en">
<head>
<meta charset="utf-8">
<title>Summit Fairway Swing Institute – Business Card</title>
<link rel="stylesheet" href="https://fonts.googleapis.com/css2?family=Roboto:wght@400;500;700&display=swap">
<style>
  :root {
    --canvas-bg: #efe6da;
    --card-bg: #ffffff;
    --brand-red: #c8191f;
    --ink: #2f2f2f;
    --ink-soft: #4a4a4a;
    --rule: #8a8a8a;
  }
  html, body {
    margin: 0;
    padding: 0;
    width: 1200px;
    height: 965px;
    overflow: hidden;
    background: var(--canvas-bg);
    font-family: "Roboto", Arial, sans-serif;
  }
  .canvas {
    position: relative;
    width: 1200px;
    height: 965px;
  }
  .card {
    position: absolute;
    left: 160px;
    top: 232px;
    width: 880px;
    height: 500px;
    background: var(--card-bg);
    border-radius: 34px;
    box-shadow: 0 10px 24px rgba(0,0,0,0.18);
    overflow: hidden;
  }
  .card__tab {
    position: absolute;
    left: 0;
    top: 200px;
    width: 14px;
    height: 128px;
    background: var(--brand-red);
  }
  .brand {
    position: absolute;
    left: 30px;
    top: 100px;
    width: 470px;
    text-align: center;
  }
  .brand__mark {
    display: block;
    margin: 0 auto 18px;
    width: 150px;
    height: 150px;
  }
  .brand__name {
    margin: 0;
    color: var(--brand-red);
    font-weight: 700;
    font-size: 38px;
    line-height: 1.08;
    letter-spacing: 0.5px;
    text-transform: uppercase;
  }
  .brand__tagline {
    display: flex;
    align-items: center;
    gap: 12px;
    margin-top: 10px;
    color: var(--brand-red);
    font-size: 19px;
    font-weight: 500;
    white-space: nowrap;
  }
  .brand__tagline::before,
  .brand__tagline::after {
    content: "";
    flex: 1;
    height: 2px;
    background: var(--rule);
  }
  .person {
    position: absolute;
    left: 535px;
    top: 92px;
  }
  .person__name {
    margin: 0;
    color: var(--brand-red);
    font-size: 31px;
    font-weight: 700;
  }
  .person__role {
    margin: 8px 0 0;
    color: var(--ink);
    font-size: 26px;
    font-weight: 400;
  }
  .contacts {
    position: absolute;
    left: 547px;
    top: 285px;
    margin: 0;
    padding: 0;
    list-style: none;
  }
  .contacts__item {
    display: flex;
    align-items: center;
    height: 36px;
    color: var(--ink-soft);
    font-size: 22px;
    white-space: nowrap;
  }
  .contacts__icon {
    width: 20px;
    height: 20px;
    margin-right: 14px;
    flex: none;
  }
</style>
</head>
<body>
<main class="canvas">
  <section class="card" aria-label="Business card">
    <div class="card__tab"></div>

    <div class="brand">
      <svg class="brand__mark" viewBox="0 0 150 150" aria-hidden="true">
        <circle cx="75" cy="75" r="72" fill="var(--brand-red)"/>
      </svg>
      <h1 class="brand__name">Summit Fairway<br>Swing Institute</h1>
      <div class="brand__tagline">Elevating Every Swing</div>
    </div>

    <div class="person">
      <h2 class="person__name">Brian Lockwell</h2>
      <p class="person__role">Founder</p>
    </div>

    <ul class="contacts">
      <li class="contacts__item">
        <svg class="contacts__icon" viewBox="0 0 20 20" aria-hidden="true">
          <path d="M5 2 L8 2 L9 6 L7 8 Q9 12 12 13 L14 11 L18 12 L18 15 Q17 18 14 18 Q4 16 2 5 Q2 2 5 2 Z" fill="var(--brand-red)"/>
        </svg>
        877-402-5518
      </li>
      <li class="contacts__item">
        <svg class="contacts__icon" viewBox="0 0 20 20" aria-hidden="true">
          <rect x="5" y="1" width="10" height="18" rx="2" fill="var(--brand-red)"/>
          <rect x="7" y="4" width="6" height="9" fill="#fff"/>
          <circle cx="10" cy="16" r="1.2" fill="#fff"/>
        </svg>
        954-310-2846
      </li>
      <li class="contacts__item">
        <svg class="contacts__icon" viewBox="0 0 20 20" aria-hidden="true">
          <text x="10" y="16" text-anchor="middle" font-size="18" font-weight="700" font-family="Roboto, Arial, sans-serif" fill="var(--brand-red)">@</text>
        </svg>
        brian@sfsinstitute.net
      </li>
      <li class="contacts__item">
        <svg class="contacts__icon" viewBox="0 0 20 20" aria-hidden="true">
          <g fill="none" stroke="var(--brand-red)" stroke-width="1.6">
            <circle cx="10" cy="10" r="8"/>
            <ellipse cx="10" cy="10" rx="3.5" ry="8"/>
            <line x1="2" y1="10" x2="18" y2="10"/>
          </g>
        </svg>
        www.sfsinstitute.net
      </li>
    </ul>
  </section>
</main>
</body>
</html>
```